Occupational Therapy Clinic Advertisement

Create an advertisement for a magazine. Below I have attached my original ad (Ad 2020.pdf) . I want the ad changed and it should be eye catching. I would like a eye catching graphics added in the ad. It should be a graphic image that applies to education. I am attaching a sample graphic image of that I liked from someone elses ad- it should not be the same- it just is there to show what I like. Please use the same words from my original ad.Dimensions: 3.75in x 10.3 in

Target Market(s)

Parents of School aged children

Requirements
Must have
• Must have eye catching Graphic. Colors should be eye catching for a typed magazine.

```html
<!DOCTYPE html>
<html lang="en">
<head>
<meta charset="utf-8">
<title>Bright Steps OT Services – Yes your child will succeed in school</title>
<link rel="stylesheet" href="https://fonts.googleapis.com/css2?family=Source+Sans+3:wght@300;400;700;900&family=Yellowtail&family=Arimo:wght@400;700&display=swap">
<style>
  :root{
    --orange:#f58a25;
    --red:#e84755;
    --maroon:#8d1a3c;
    --navy:#0a4f82;
    --sky:#3ab0e0;
    --teal:#5cc6d6;
    --title:#0f4675;
    --accent-red:#b8202e;
    --number:#c4c4c4;
    --ink:#111;
    --white:#fff;
    --bg-light:#f4f4f4;
    --bg-dark:#8e8e8e;
  }
  *{box-sizing:border-box;margin:0;padding:0}
  html,body{width:785px;height:1200px;overflow:hidden;background:#fff}
  .ad{position:relative;width:785px;height:1200px;overflow:hidden;
      background:radial-gradient(ellipse at 50% 52%,var(--bg-light) 0%,#d2d2d2 45%,var(--bg-dark) 100%);
      font-family:"Source Sans 3",sans-serif}
  .hex-layer{position:absolute;left:0;top:0}
  .hex-text{position:absolute;width:290px;margin-left:-145px;text-align:center;color:var(--white);
      font-weight:300;font-size:27px;line-height:35px}
  .hex-text b{font-weight:700}
  .hex-num{position:absolute;width:120px;margin-left:-60px;text-align:center;color:var(--number);
      font-weight:300;font-size:58px;line-height:58px;opacity:.9}
  .headline{position:absolute;left:180px;top:392px;width:425px;text-align:center;color:var(--title);
      font-weight:700;font-size:50px;line-height:64px;letter-spacing:-1.5px}
  .headline .struck{position:relative;display:inline-block}
  .headline .struck::after{content:"";position:absolute;left:-4px;right:-2px;top:52%;height:3px;
      background:var(--accent-red);transform:rotate(-14deg)}
  .headline .will{position:absolute;left:-62px;top:-14px;font-family:"Yellowtail",cursive;font-weight:400;
      color:var(--accent-red);font-size:44px;letter-spacing:0;transform:rotate(-8deg)}
  .color-bar{position:absolute;left:229px;top:594px;width:327px;height:6px;display:flex}
  .color-bar span{flex:1}
  .clinic-name{position:absolute;left:240px;top:626px;width:305px;text-align:center;color:var(--accent-red);
      font-weight:700;font-size:22px;line-height:28px;letter-spacing:.5px}
  .footer{position:absolute;left:0;top:1010px;width:785px;height:190px;background:var(--ink)}
  .seal{position:absolute;left:26px;top:967px;width:144px;height:144px;border-radius:50%;background:var(--white)}
  .seal .mark{position:absolute;left:32px;top:32px;width:80px;height:80px;border-radius:50%;background:#7fbf3f}
  .age{position:absolute;left:608px;top:967px;width:144px;height:144px;border-radius:50%;background:var(--white);
      text-align:center;font-family:"Arimo",sans-serif;color:#222}
  .age svg{display:block;margin:22px auto 4px}
  .age .label{font-size:13px;font-weight:700}
  .age .range{font-size:28px;font-weight:700;line-height:32px}
  .contact{position:absolute;left:195px;top:1030px;width:400px;color:var(--white);
      font-family:"Arimo",sans-serif;font-size:14.5px;line-height:19px}
  .contact b{font-weight:700}
  .therapist{position:absolute;left:0;top:1141px;width:785px;text-align:center;color:var(--white);
      font-family:"Arimo",sans-serif;font-size:31px}
</style>
</head>
<body>
<div class="ad">
  <svg class="hex-layer" width="785" height="1200" viewBox="0 0 785 1200">
    <defs>
      <linearGradient id="sheen" x1="0" y1="0" x2="0" y2="1">
        <stop offset="0" stop-color="#fff" stop-opacity=".18"/>
        <stop offset=".7" stop-color="#fff" stop-opacity="0"/>
        <stop offset=".7" stop-color="#000" stop-opacity=".06"/>
        <stop offset="1" stop-color="#000" stop-opacity=".08"/>
      </linearGradient>
    </defs>
    <g class="hexes">
      <polygon fill="var(--orange)" points="223,45 378,134.5 378,313.5 223,403 68,313.5 68,134.5"/>
      <polygon fill="var(--red)" points="565,45 720,134.5 720,313.5 565,403 410,313.5 410,134.5"/>
      <polygon fill="var(--teal)" points="51,342 206,431.5 206,610.5 51,700 -104,610.5 -104,431.5"/>
      <polygon fill="var(--maroon)" points="738,342 893,431.5 893,610.5 738,700 583,610.5 583,431.5"/>
      <polygon fill="var(--sky)" points="223,640 378,729.5 378,908.5 223,998 68,908.5 68,729.5"/>
      <polygon fill="var(--navy)" points="565,640 720,729.5 720,908.5 565,998 410,908.5 410,729.5"/>
    </g>
    <g fill="url(#sheen)">
      <polygon points="223,45 378,134.5 378,313.5 223,403 68,313.5 68,134.5"/>
      <polygon points="565,45 720,134.5 720,313.5 565,403 410,313.5 410,134.5"/>
      <polygon points="51,342 206,431.5 206,610.5 51,700 -104,610.5 -104,431.5"/>
      <polygon points="738,342 893,431.5 893,610.5 738,700 583,610.5 583,431.5"/>
      <polygon points="223,640 378,729.5 378,908.5 223,998 68,908.5 68,729.5"/>
      <polygon points="565,640 720,729.5 720,908.5 565,998 410,908.5 410,729.5"/>
    </g>
    <g class="icons" fill="#fff">
      <!-- briefcase -->
      <rect x="202" y="84" width="42" height="30" rx="3"/>
      <rect x="214" y="78" width="18" height="8" rx="2" fill="none" stroke="#fff" stroke-width="3"/>
      <rect x="219" y="95" width="8" height="6" fill="var(--orange)"/>
      <!-- people -->
      <circle cx="565" cy="89" r="8"/><path d="M551 114a14 12 0 0 1 28 0z"/>
      <circle cx="547" cy="95" r="6"/><path d="M535 114a12 10 0 0 1 24 0z"/>
      <circle cx="583" cy="95" r="6"/><path d="M571 114a12 10 0 0 1 24 0z"/>
      <!-- bar chart -->
      <rect x="30" y="376" width="7" height="38"/><rect x="40" y="384" width="7" height="30"/>
      <rect x="50" y="394" width="7" height="20"/><rect x="60" y="400" width="7" height="14"/>
      <!-- line chart -->
      <polyline points="716,412 728,392 740,404 756,390" fill="none" stroke="#fff" stroke-width="3"/>
      <circle cx="716" cy="412" r="3.5"/><circle cx="728" cy="392" r="3.5"/><circle cx="740" cy="404" r="3.5"/><circle cx="756" cy="390" r="3.5"/>
      <!-- percent -->
      <circle cx="214" cy="686" r="6"/><circle cx="232" cy="704" r="6"/>
      <path d="M234 680l5 4-25 28-5-4z"/>
      <!-- pie -->
      <circle cx="565" cy="696" r="17"/>
      <path d="M565 679v17h17a17 17 0 0 0-17-17z" fill="var(--navy)"/>
      <path d="M567 677v17h17a17 17 0 0 0-17-17z"/>
    </g>
  </svg>

  <div class="hex-text" style="left:223px;top:154px">Does Your Child<br>Struggle with<br>Reading/kriah?</div>
  <div class="hex-text" style="left:565px;top:154px">Knows The<br>Information But<br>Fails The Test?</div>
  <div class="hex-text" style="left:693px;top:452px">Has Difficulty<br>Remembering<br>Names and<br>Dates?</div>
  <div class="hex-text" style="left:104px;top:452px"><b>We Treat</b>:<br>The Underlying<br>Processing<br>Deficits</div>
  <div class="hex-text" style="left:223px;top:751px"><b>We Treat</b>:<br>Using<br>Researched Based<br>Techniques</div>
  <div class="hex-text" style="left:565px;top:751px"><b>We Evaluate</b>:<br>Using<br>Standardized<br>Evaluations</div>

  <div class="hex-num" style="left:222px;top:322px">01</div>
  <div class="hex-num" style="left:565px;top:322px">02</div>
  <div class="hex-num" style="left:736px;top:622px">03</div>
  <div class="hex-num" style="left:565px;top:919px">04</div>
  <div class="hex-num" style="left:222px;top:919px">05</div>
  <div class="hex-num" style="left:51px;top:618px">06</div>

  <h1 class="headline">Yes your child<br><span class="struck"><span class="will">Will</span>can</span> succeed<br>in school!</h1>

  <div class="color-bar">
    <span style="background:var(--orange)"></span><span style="background:var(--red)"></span>
    <span style="background:var(--maroon)"></span><span style="background:var(--navy)"></span>
    <span style="background:var(--sky)"></span><span style="background:var(--teal)"></span>
  </div>

  <div class="clinic-name">BRIGHT STEPS<br>OT Services</div>

  <div class="footer"></div>
  <div class="seal"><div class="mark"></div></div>
  <div class="contact">Located in Borough Park, evaluations are done in Borough Park &amp; Staten Island. For more information or to be added to our email list, please email: <b>brightstepsot@example.com</b> or call <b>(555) 014-2286</b></div>
  <div class="age">
    <svg width="60" height="28" viewBox="0 0 60 28" fill="#2a3a8f">
      <circle cx="18" cy="7" r="7"/><path d="M4 28a14 13 0 0 1 28 0z"/>
      <circle cx="42" cy="7" r="7"/><path d="M28 28a14 13 0 0 1 28 0z"/>
    </svg>
    <div class="label">Age of Child:</div>
    <div class="range">6 - 18</div>
  </div>
  <div class="therapist">Dina Halpern OTR/L</div>
</div>
</body>
</html>
```